Tides of the barrio "Las mareas del barrio nuevo"

I'm writing a book about word of mouth and the consumer as the media "the book is in Spanish" so you have to use "Las mareas del barrio nuevo" the subtitle is and 30 examples that proves it "Con doce relatos de esquina"

Book is about the power of consumer nowadays , the book will combine the era of social media but also the power of one to one word of mouth meaning w/o being connected to an electronic platform

Tides of the new barrio is a book about the power that now the consumer has in this double way interaction between the brands and the consumer, between the services and the people between the social media and the traditional media.

Consumer is on control and it is because "tides of the new barrio"

About book principles
I love simple books white background, simplicity around the fonts and the images (simple is better)

Target Market(s)

Marketing and digital marketing managers, social media managers, community managers, social media agencies, business people

Industry/Entity Type

Electronic

Requirements
Must have
• White backgroung, black and red fonts big fonts
Nice to have
• the subtitle "Con doce relatos de la calle"

```html
<!DOCTYPE html>
<html lang="es">
<head>
<meta charset="utf-8">
<title>Las mareas del barrio nuevo — cubierta</title>
<link rel="stylesheet" href="https://fonts.googleapis.com/css2?family=Anton&family=Questrial&display=swap">
<style>
  :root {
    --backdrop: #e9e7e4;
    --paper: #ffffff;
    --ink: #141414;
    --accent: #d10a0a;
    --shade: rgba(0, 0, 0, 0.18);
  }
  * { box-sizing: border-box; margin: 0; padding: 0; }
  html, body {
    width: 1200px;
    height: 983px;
    overflow: hidden;
    background: var(--backdrop);
  }
  .stage {
    position: relative;
    width: 1200px;
    height: 983px;
  }
  .cover {
    position: absolute;
    left: 300px;
    top: 52px;
    width: 600px;
    height: 880px;
    background: var(--paper);
    box-shadow: 0 10px 30px var(--shade);
    color: var(--ink);
  }
  .tagline {
    position: absolute;
    top: 58px;
    left: 0;
    right: 0;
    text-align: center;
    font-family: "Questrial", sans-serif;
    font-size: 17px;
    letter-spacing: 0.12em;
    text-transform: uppercase;
  }
  .title-block {
    position: absolute;
    left: 70px;
    top: 170px;
    width: 470px;
  }
  .title-top {
    display: flex;
    align-items: flex-end;
    gap: 22px;
  }
  .title-word {
    display: block;
    font-family: "Anton", sans-serif;
    text-transform: uppercase;
    line-height: 0.92;
  }
  .title-word--lead {
    font-size: 170px;
    color: var(--ink);
  }
  .cover-art {
    width: 150px;
    height: 140px;
    margin-bottom: 12px;
  }
  .title-word--accent {
    font-size: 132px;
    color: var(--accent);
    margin-top: 8px;
  }
  .title-word--tail {
    font-size: 60px;
    color: var(--ink);
    margin-top: 8px;
    letter-spacing: 0.01em;
  }
  .subtitle {
    margin-top: 26px;
    font-family: "Questrial", sans-serif;
    font-size: 21px;
    letter-spacing: 0.04em;
    text-transform: uppercase;
    color: var(--accent);
  }
  .author {
    position: absolute;
    right: 70px;
    bottom: 110px;
    font-family: "Questrial", sans-serif;
    font-size: 22px;
    letter-spacing: 0.28em;
    text-transform: uppercase;
    color: var(--ink);
  }
</style>
</head>
<body>
<main class="stage">
  <section class="cover">
    <p class="tagline">El poder de uno a uno el boca a boca</p>

    <div class="title-block">
      <div class="title-top">
        <span class="title-word title-word--lead">Las</span>
        <svg class="cover-art" viewBox="0 0 150 140" role="img" aria-label="Ilustración de siluetas de personas en rojo y negro dentro de un marco">
          <rect x="4" y="22" width="112" height="112" fill="none" stroke="var(--ink)" stroke-width="7"/>
          <rect x="30" y="4" width="116" height="120" fill="var(--accent)"/>
          <rect x="62" y="30" width="70" height="104" fill="var(--ink)"/>
        </svg>
      </div>
      <span class="title-word title-word--accent">Mareas</span>
      <span class="title-word title-word--tail">del barrio nuevo</span>
      <p class="subtitle">Con doce relatos de la calle</p>
    </div>

    <p class="author">Lucas Arrieta</p>
  </section>
</main>
</body>
</html>
```